Redesign of Pledgebloom.com

We need a redesign of some key-pages on our crowdfunding website for mobile apps, PledgeBloom.com.

- Redesign of homepage
http://www.pledgebloom.com/en

- Redesign of project submission page
http://www.pledgebloom.com/en/submit-your-app/submit-your-app

- Redesign of browsing section
http://www.pledgebloom.com/en/fund-apps

- Redesign of project funding page
http://www.pledgebloom.com/en/fund-apps/sponsor/sketch-riddler?amount=5.00

Design should be highly focused on a great user experience for users of the platform, being in principal mobile developers. So we need a great user experience for mobile developers using our service.

Benchmark designs we particularly like are:
http://www.brimwagon.com/
http://www.tradeyourtool.com/landing/
http://www.vovari.com/

Design should have a more 'fun, happy to get involved' factor as it has nox.
Updates

Target Market(s)

mobile app developers

Industry/Entity Type

Crowdfunding

Requirements
Must have
• Submission forms must have explanation fields next to the form

Homepage should have design in whihc a introductary video can be integrated

```html
<!DOCTYPE html>
<html lang="en">
<head>
<meta charset="utf-8">
<title>PledgeBloom – Crowdfunding for Mobile Apps</title>
<link rel="stylesheet" href="https://fonts.googleapis.com/css2?family=Bree+Serif&family=Ubuntu:wght@400;500&family=PT+Sans:ital,wght@0,400;0,700;1,400&display=swap">
<style>
:root{
  --header-top:#1f5aa8;
  --header-bottom:#5d9be0;
  --navy:#13305e;
  --nav-blue:#3f7fd0;
  --orange:#f7941d;
  --hero-light:#eaf4fd;
  --hero-mid:#a9d0f3;
  --green:#4b7a1e;
  --text:#222;
  --muted:#444;
  --panel-line:#c9d8ea;
  --footer:#7f9fea;
  --footer-deep:#6d8fe3;
  --footer-bar:#aac1f3;
  --white:#fff;
}
*{box-sizing:border-box;margin:0;padding:0}
html,body{width:736px;height:1200px;overflow:hidden}
body{position:relative;background:#e9eef7;font-family:"PT Sans",Arial,sans-serif;color:var(--text)}
.abs{position:absolute}

/* header */
.site-header{left:0;top:0;width:736px;height:86px;background:linear-gradient(var(--header-top),var(--header-bottom));border-top:3px solid var(--navy)}
.brand{left:32px;top:26px;display:flex;align-items:center;gap:7px;color:var(--white);font-family:"Ubuntu",sans-serif;font-size:17px}
.brand-mark{width:20px;height:26px;background:var(--white)}
.lang{left:514px;top:6px;color:var(--white);font-size:9px}
.top-links{left:562px;top:-3px;width:148px;height:27px;background:var(--navy);border-radius:0 0 3px 3px;display:flex;justify-content:space-around;align-items:center;color:var(--white);font-size:8.5px;padding-top:3px}
.social{top:45px;width:20px;height:20px;border-radius:50%;background:var(--white)}
.search{left:548px;top:46px;width:166px;height:20px;background:var(--white);border-radius:2px;font-size:8px;font-style:italic;color:#777;padding:5px 8px}
.search svg{position:absolute;right:6px;top:5px}

/* nav */
.main-nav{left:26px;top:93px;width:684px;height:37px;background:linear-gradient(#5a97e0,#2f6cc0);border:1px solid #2b5ea8;display:flex;font-family:"Bree Serif",serif;font-size:12px;color:var(--white)}
.main-nav span{display:flex;align-items:center;justify-content:center;border-right:1px solid #6ea4e4}
.main-nav .active{background:linear-gradient(#fca833,#ef7f0c)}

/* hero */
.hero{left:15px;top:86px;width:705px;height:326px;background:linear-gradient(100deg,var(--hero-light) 0%,var(--hero-mid) 45%,var(--hero-light) 100%)}
.video-device{left:56px;top:148px;width:306px;height:242px;background:#1b1b1b;border-radius:14px;border:3px solid #c9ccd1}
.video-screen{left:83px;top:175px;width:255px;height:183px;background:linear-gradient(#16305a,#0d1f3d)}
.hero-title{left:402px;top:178px;font-family:"Bree Serif",serif;font-size:22px;line-height:27px;color:var(--navy)}
.hero-lead{left:402px;top:237px;font-size:11px;color:var(--navy)}
.hero-text{left:402px;top:254px;width:290px;font-size:9px;line-height:12px;color:var(--navy)}
.btn{display:flex;align-items:center;justify-content:center;color:var(--white);font-size:11px;font-weight:700;border-radius:2px}
.btn-project{left:401px;top:310px;width:101px;height:25px;background:var(--navy)}
.btn-support{left:510px;top:310px;width:101px;height:25px;background:var(--orange)}

/* content */
.content{left:15px;top:412px;width:705px;height:552px;background:var(--white)}
.section-title{left:31px;font-family:"Ubuntu",sans-serif;font-size:13.5px;color:#111}
.section-sub{left:31px;font-size:8px;color:var(--muted)}
.app-row{left:31px;display:flex;gap:14px}
.app-tile{width:77px;height:67px}
.divider{left:25px;width:441px;border-top:1px dotted #888}

.side-panel{left:494px;border:1px solid var(--panel-line);background:var(--white)}
.support{top:420px;width:218px;height:188px;padding:13px 16px}
.panel-title{font-family:"Ubuntu",sans-serif;font-size:14.5px;color:#111}
.support p{font-size:8px;line-height:11px;margin-top:7px}
.support h4{font-size:10px;color:var(--green);margin-top:9px}
.support ul{list-style:none;margin-top:4px}
.support li{font-size:7.5px;display:flex;align-items:center;gap:5px;height:14.5px}
.btn-green{position:absolute;left:16px;top:154px;width:80px;height:20px;background:var(--green);font-size:7.5px;font-weight:400}
.ask-tab{left:708px;top:412px;width:28px;height:82px;background:#5f9434;border:1px solid #fff;color:var(--white);font-family:"Ubuntu",sans-serif;font-size:12px;display:flex;align-items:center;justify-content:center}
.ask-tab span{transform:rotate(-90deg);white-space:nowrap}

.community{top:617px;width:218px;height:208px}
.community-thumb{left:10px;top:12px;width:48px;height:40px;background:linear-gradient(#23467e,#4f7fc0)}
.community-name{left:65px;top:9px;font-size:10px;color:var(--navy)}
.like-btn{left:65px;top:28px;width:37px;height:17px;border:1px solid #bbb;background:#eef1f6;border-radius:2px;font-size:7.5px;color:#3a5da0;display:flex;align-items:center;justify-content:center}
.fans-count{left:11px;top:63px;font-size:9px}
.fan{width:42px}
.fan-photo{width:42px;height:38px}
.fan-name{font-size:6.5px;color:var(--navy);margin-top:2px}

/* partners */
.partners-rule{left:28px;top:870px;width:680px;border-top:1px solid #c8c8c8}
.partners-title{left:322px;top:862px;padding:0 8px;background:var(--white);font-family:"Ubuntu",sans-serif;font-size:12.5px;color:#222}
.partner-row{left:40px;top:888px;width:650px;height:40px;display:flex;align-items:center;justify-content:space-between;font-family:"Ubuntu",sans-serif;font-size:13px;color:#444}
.partner-badge{width:38px;height:38px;border-radius:50%;background:#3d6b2e}

/* footer */
.site-footer{left:0;top:964px;width:736px;height:198px;background:linear-gradient(var(--footer),var(--footer-deep));border-top:1px dashed #4d6fc0}
.scissors{left:18px;top:955px;font-size:14px;color:var(--navy)}
.footer-title{top:984px;font-family:"Ubuntu",sans-serif;font-size:11px;color:var(--navy)}
.quick-link{font-size:8px;color:var(--white)}
.quick-link::before{content:"›";margin-right:6px}
.footer-rule{top:985px;height:145px;border-left:1px solid #9fb5ee}
.blog-text{left:242px;width:220px;font-size:8px;line-height:10.5px;font-style:italic;color:var(--white)}
.blog-date{left:242px;font-size:8px;color:var(--navy)}
.field{left:508px;width:191px;background:var(--white);border:1px solid #c8d4f2;font-size:7.5px;color:#555;padding:3px 8px}
.btn-submit{left:510px;top:1116px;width:54px;height:20px;background:var(--navy);font-size:9px}
.footer-bar{left:0;top:1162px;width:736px;height:38px;background:var(--footer-bar);font-size:7.5px;color:var(--navy);padding:12px 18px}
</style>
</head>
<body>

<header class="abs site-header">
  <div class="abs brand"><span class="brand-mark"></span>PledgeBloom</div>
  <div class="abs lang">English ▾</div>
  <nav class="abs top-links"><span>Blog</span><span>Get AAA Certified</span><span>About Us</span></nav>
  <span class="abs social" style="left:495px" aria-label="Social profile"></span>
  <span class="abs social" style="left:519px" aria-label="Social profile"></span>
  <div class="abs search">enter keyword
    <svg width="10" height="10" viewBox="0 0 10 10"><circle cx="4" cy="4" r="3" fill="none" stroke="#1f5aa8" stroke-width="1.6"/><line x1="6.3" y1="6.3" x2="9.3" y2="9.3" stroke="#1f5aa8" stroke-width="1.8"/></svg>
  </div>
</header>

<section class="abs hero"></section>
<nav class="abs main-nav">
  <span class="active" style="width:87px">Home</span>
  <span style="width:95px">Fund App</span>
  <span style="width:128px">Submit you App</span>
  <span style="width:135px">Find a Developer</span>
  <span style="width:119px">Hot iw Works</span>
  <span style="width:120px;border-right:0">Register</span>
</nav>

<div class="abs video-device"></div>
<div class="abs video-screen" role="img" aria-label="Introductory video showing the app on a tablet"></div>
<svg class="abs" style="left:184px;top:235px" width="52" height="52" viewBox="0 0 52 52"><circle cx="26" cy="26" r="24" fill="rgba(0,0,0,.45)" stroke="#fff" stroke-width="2"/><path d="M20 15 L37 26 L20 37 Z" fill="#fff"/></svg>

<h1 class="abs hero-title">Our Apps Mobile Funder<br>Punch Line goes here</h1>
<p class="abs hero-lead">Lorem ipsum dolor sit amet, consectetuer adipiscing elit.</p>
<p class="abs hero-text">Nullam enim leo, egestas id, condimentum at, laoreet mattis, massa. Sed eleifend nonummy diam. Praesent mauris ante, elementum et, bibendum at, posuere sit amet, nibh.</p>
<div class="abs btn btn-project">Start Project</div>
<div class="abs btn btn-support">Start Supporting</div>

<main class="abs content"></main>

<h2 class="abs section-title" style="top:429px">Most Funded Apps</h2>
<p class="abs section-sub" style="top:447px">Lorem ipsum dolor sit amet, consectetuer</p>
<div class="abs app-row" style="top:468px">
  <div class="app-tile" role="img" aria-label="Chalkboard puzzle game icon" style="background:#2b2b2b"></div>
  <div class="app-tile" role="img" aria-label="Coloured pencils app icon" style="background:#f3f0d2"></div>
  <div class="app-tile" role="img" aria-label="Cartoon city game icon" style="background:#86b8df"></div>
  <div class="app-tile" role="img" aria-label="Cartoon mascot game icon" style="background:#c7202b"></div>
  <div class="app-tile" role="img" aria-label="Wireless letter app icon" style="background:#4a4a4a"></div>
</div>
<div class="abs divider" style="top:555px"></div>

<h2 class="abs section-title" style="top:572px">Our Staff’s Packs</h2>
<p class="abs section-sub" style="top:591px">Lorem ipsum dolor sit amet, consectetuer</p>
<div class="abs app-row" style="top:610px">
  <div class="app-tile" role="img" aria-label="Cartoon robot game icon" style="background:#d98c3c"></div>
  <div class="app-tile" role="img" aria-label="Cartoon mascot game icon" style="background:#c7202b"></div>
  <div class="app-tile" role="img" aria-label="Football helmet app icon" style="background:#7b7b7b"></div>
  <div class="app-tile" role="img" aria-label="Wireless letter app icon" style="background:#4a4a4a"></div>
  <div class="app-tile" role="img" aria-label="Jewel puzzle game icon" style="background:#2d6d3a"></div>
</div>
<div class="abs divider" style="top:698px"></div>

<h2 class="abs section-title" style="top:714px">Succesfully Funded</h2>
<p class="abs section-sub" style="top:733px">Lorem ipsum dolor sit amet, consectetuer</p>
<div class="abs app-row" style="top:755px">
  <div class="app-tile" role="img" aria-label="Football helmet app icon" style="background:#7b7b7b"></div>
  <div class="app-tile" role="img" aria-label="Thermometer on phone app icon" style="background:#c9a087"></div>
  <div class="app-tile" role="img" aria-label="Copyright symbol app icon" style="background:#d9d9d9"></div>
  <div class="app-tile" role="img" aria-label="Coloured pencils app icon" style="background:#f3f0d2"></div>
  <div class="app-tile" role="img" aria-label="Jewel puzzle game icon" style="background:#2d6d3a"></div>
</div>

<aside class="abs side-panel support">
  <h3 class="panel-title">Support New Mobile apps</h3>
  <p>Pellentesque habitant morbi tristique senectus et netus et malesuada fames ac turpis egestas. In posuere felis nec tortor. Pellentesque faucibus.</p>
  <h4>App Builders:</h4>
  <ul>
    <li><svg width="8" height="8" viewBox="0 0 8 8"><circle cx="4" cy="4" r="4" fill="#5f9434"/><path d="M4 2v4M2 4h4" stroke="#fff" stroke-width="1.2"/></svg>Fund your development</li>
    <li><svg width="8" height="8" viewBox="0 0 8 8"><circle cx="4" cy="4" r="4" fill="#5f9434"/><path d="M4 2v4M2 4h4" stroke="#fff" stroke-width="1.2"/></svg>Build up customers</li>
    <li><svg width="8" height="8" viewBox="0 0 8 8"><circle cx="4" cy="4" r="4" fill="#5f9434"/><path d="M4 2v4M2 4h4" stroke="#fff" stroke-width="1.2"/></svg>Keep 100% ownership</li>
  </ul>
  <div class="btn btn-green">START PROJECT</div>
</aside>
<div class="abs ask-tab"><span>Ask Us</span></div>

<aside class="abs side-panel community">
  <div class="abs community-thumb" role="img" aria-label="PledgeBloom page thumbnail"></div>
  <div class="abs community-name">PledgeBloom Crowdfunding</div>
  <div class="abs like-btn">Like</div>
  <div class="abs fans-count">2265 people likes PledgeBloom</div>
  <div class="abs fan" style="left:10px;top:86px"><div class="fan-photo" role="img" aria-label="Supporter photo" style="background:#b07a5e"></div><div class="fan-name">R. Dale</div></div>
  <div class="abs fan" style="left:60px;top:86px"><div class="fan-photo" role="img" aria-label="Supporter avatar, globe" style="background:#4f7fb8"></div><div class="fan-name">M. Orin</div></div>
  <div class="abs fan" style="left:110px;top:86px"><div class="fan-photo" role="img" aria-label="Supporter photo" style="background:#6e7a5a"></div><div class="fan-name">Lena</div></div>
  <div class="abs fan" style="left:159px;top:86px"><div class="fan-photo" role="img" aria-label="Supporter photo" style="background:#8a8a8a"></div><div class="fan-name">Tova K</div></div>
  <div class="abs fan" style="left:10px;top:142px"><div class="fan-photo" role="img" aria-label="Supporter photo" style="background:#a0644c"></div><div class="fan-name">Brenn</div></div>
  <div class="abs fan" style="left:60px;top:142px"><div class="fan-photo" role="img" aria-label="Supporter photo" style="background:#9aa0a6"></div><div class="fan-name">Brenn</div></div>
  <div class="abs fan" style="left:110px;top:142px"><div class="fan-photo" role="img" aria-label="Supporter avatar placeholder" style="background:#13305e"></div><div class="fan-name">Brenn</div></div>
  <div class="abs fan" style="left:159px;top:142px"><div class="fan-photo" role="img" aria-label="Supporter avatar, emblem" style="background:#5a8fc4"></div><div class="fan-name">Hollis</div></div>
</aside>

<div class="abs partners-rule"></div>
<h3 class="abs partners-title">Our Partners:</h3>
<div class="abs partner-row">
  <span>Harbor Owls</span>
  <span class="partner-badge" aria-label="Partner badge"></span>
  <span>Kestrel Corp</span>
  <span>Amber Comet</span>
  <span>Lumavo</span>
  <span>Ortho Lab</span>
  <span>QXNet</span>
  <span>Pagewire</span>
</div>

<footer class="abs site-footer"></footer>
<div class="abs scissors">✂</div>

<h3 class="abs footer-title" style="left:24px">Quick Links</h3>
<span class="abs quick-link" style="left:26px;top:1007px">Home</span>
<span class="abs quick-link" style="left:26px;top:1026px">About Us</span>
<span class="abs quick-link" style="left:26px;top:1045px">Offers</span>
<span class="abs quick-link" style="left:26px;top:1064px">Experience</span>
<span class="abs quick-link" style="left:26px;top:1083px">Contact Us</span>
<span class="abs quick-link" style="left:116px;top:1007px">Our Partners</span>
<span class="abs quick-link" style="left:116px;top:1026px">Featured On</span>
<span class="abs quick-link" style="left:116px;top:1045px">How it Works</span>
<span class="abs quick-link" style="left:116px;top:1064px">Support</span>
<span class="abs quick-link" style="left:116px;top:1083px">FAQ</span>
<div class="abs footer-rule" style="left:216px"></div>

<h3 class="abs footer-title" style="left:242px">Recent Blog Post</h3>
<p class="abs blog-text" style="top:1002px">Lorem ipsum dolor sit amet, consectetuer adipiscing elit. Nam cursus. Morbi ut mi. Nullam enim leo, egestas id, condimentum at,</p>
<p class="abs blog-date" style="top:1040px">Posted 2 hour ago</p>
<p class="abs blog-text" style="top:1060px">Lorem ipsum dolor sit amet, consectetuer adipiscing elit. Nam cursus. Morbi ut mi. Nullam enim leo, egestas id, condimentum at,</p>
<p class="abs blog-date" style="top:1098px">Posted 2 hour ago</p>
<div class="abs footer-rule" style="left:481px"></div>

<h3 class="abs footer-title" style="left:506px">Contact Us Now</h3>
<div class="abs field" style="top:1008px;height:17px">type your name</div>
<div class="abs field" style="top:1031px;height:18px">type your email address</div>
<div class="abs field" style="top:1055px;height:55px">your message</div>
<div class="abs btn btn-submit">Submit</div>

<div class="abs footer-bar">© 2012 Company Name &nbsp;|&nbsp; All right reserved &nbsp;|&nbsp; Term &amp; Conditions</div>

</body>
</html>
```